Quiz Arena Duel Halls Initial Post Card

Looking for an oversized post card design to send out via RMCD with NPDS. Looking for this postcard to match the look and feel of our logo/website. This is a new business that we are launching and this is the first piece of marketing we are working on to get our name out there. See below for additional requirements of the postcard.

1. Must match the look and feel of our website/logo
2. Must have two coupons outlined - details on both are attached
3. Must have callout somewhere - that stands out - that says "#1 New Experience in the Twin Cities"
4. Must call out "Great for team building, work outings,birthday celebrations, or just for fun with friends and family!"
5. Call out "Private team building events available upon request" and "Online bookings available now!"
6. Call out in big letters "Finally YOU"RE ALL IN in the QUIZ ARENA!"
7. Callout website - www.quizarenaduelhalls.example, Phone # 555-318-2741, facebook @QuizArenaDuelHalls, Address: 4127 Larkmoor Rd S, Cedar Hollow, MN
8. Must callout the requirements for RMCD - let me know if you are not aware of these. I have attached for reference.

Check out: www.quizarenaduelhalls.example for inspiration/direction.

Industry/Entity Type

Entertainment

Requirements
Must have
• Simple - not too crowded of a design. Call to action to check out our website/give us a call!
Should not have
• Too busy of a design - text everywhere is not okay.

```html
<!DOCTYPE html>
<html lang="en">
<head>
<meta charset="utf-8">
<title>Quiz Arena Duel Halls – Postcard</title>
<link rel="stylesheet" href="https://fonts.googleapis.com/css2?family=Catamaran:wght@400;600;700;800&family=Arimo:wght@400;700&display=swap">
<style>
  :root {
    --page: #e6e6e6;
    --ink-dark: #1b1c1f;
    --ink-mid: #2b2d33;
    --brand-blue: #0a84d0;
    --brand-cyan: #1ec0f0;
    --coupon-blue: #7fd6f5;
    --yellow: #f2e23a;
    --soft-blue: #7fd0f2;
    --white: #ffffff;
    --grey-text: #444;
  }
  * { box-sizing: border-box; margin: 0; padding: 0; }
  html, body { width: 976px; height: 1200px; overflow: hidden; }
  body {
    background: var(--page);
    font-family: "Catamaran", sans-serif;
    position: relative;
  }
  .card {
    position: absolute;
    left: 122px;
    width: 711px;
    height: 463px;
    overflow: hidden;
    box-shadow: 0 4px 14px rgba(0,0,0,.25);
  }
  .card--front { top: 107px; background: radial-gradient(ellipse at 50% 60%, var(--ink-mid), var(--ink-dark) 75%); }
  .card--back  { top: 622px; background: var(--white); }

  /* ---------- Front ---------- */
  .stage-lights {
    position: absolute; left: 0; top: 0; width: 711px; height: 235px;
    background:
      radial-gradient(ellipse at 20% 30%, rgba(120,180,255,.55), transparent 45%),
      radial-gradient(ellipse at 80% 30%, rgba(200,120,255,.5), transparent 45%),
      radial-gradient(ellipse at 30% 90%, rgba(255,90,120,.45), transparent 40%),
      linear-gradient(180deg, #1d2a8a 0%, #3a2fa8 45%, #5a3ab8 75%, #2f4bc4 100%);
  }
  .front-band { position: absolute; left: 0; top: 198px; }
  .brand-name {
    position: absolute;
    color: var(--white);
    font-weight: 800;
    text-align: center;
    line-height: 0.95;
    letter-spacing: 1px;
  }
  .card--front .brand-name { left: 0; width: 711px; top: 58px; font-size: 46px; }
  .headline {
    position: absolute; color: var(--yellow); font-weight: 700; white-space: nowrap;
  }
  .card--front .headline { left: 0; width: 711px; text-align: center; top: 176px; font-size: 26px; }
  .audience {
    position: absolute; left: 60px; width: 591px; top: 245px;
    text-align: center; color: var(--soft-blue); font-size: 17px; line-height: 20px;
  }
  .coupon {
    position: absolute; top: 283px; width: 205px; height: 112px;
    background: var(--coupon-blue);
    padding: 3px;
  }
  .coupon__inner {
    border: 1.5px dashed var(--ink-dark);
    height: 100%;
    padding: 4px 8px 0;
    text-align: center;
    color: var(--ink-dark);
  }
  .coupon--left { left: 40px; }
  .coupon--right { left: 465px; }
  .coupon__value { font-size: 50px; font-weight: 800; line-height: 42px; }
  .coupon__value span { font-size: 24px; }
  .coupon__code { font-size: 11.5px; font-weight: 600; margin-top: 2px; }
  .coupon__terms { font-size: 6px; line-height: 7px; margin-top: 4px; }
  .finally {
    position: absolute; left: 253px; width: 210px; top: 300px;
    text-align: center; color: var(--yellow); font-weight: 700;
    font-size: 22px; line-height: 25px;
  }
  .contact-bar {
    position: absolute; left: 0; top: 408px; width: 711px; height: 55px;
    background: linear-gradient(90deg, var(--brand-cyan), var(--brand-blue));
    display: flex; align-items: center; justify-content: space-between;
    padding: 0 14px;
    color: var(--white); font-size: 16px; font-weight: 600;
  }
  .contact-bar .item, .social .item { display: flex; align-items: center; gap: 6px; }

  /* ---------- Back ---------- */
  .back-panel { position: absolute; left: 0; top: 0; }
  .card--back .brand-name { left: 20px; width: 310px; top: 60px; font-size: 44px; }
  .card--back .headline { left: 18px; top: 212px; font-size: 22px; }
  .private {
    position: absolute; left: 28px; top: 252px; color: var(--white);
    font-size: 14px; font-weight: 700;
  }
  .online {
    position: absolute; left: 32px; width: 296px; top: 312px; text-align: center;
    color: var(--yellow); font-weight: 700; font-size: 15px;
  }
  .web-button {
    position: absolute; left: 32px; top: 345px; width: 295px; height: 39px;
    background: var(--yellow); border-radius: 12px;
    display: flex; align-items: center; justify-content: center;
    color: var(--ink-dark); font-weight: 700; font-size: 15px;
    box-shadow: 0 0 0 2px rgba(255,255,255,.7);
  }
  .social {
    position: absolute; left: 20px; top: 412px; width: 320px;
    display: flex; justify-content: space-between; align-items: center;
    color: var(--white);
  }
  .social .handle { font-size: 12.5px; }
  .social .phone { font-size: 18px; }
  .return-address {
    position: absolute; left: 418px; top: 33px; font-style: normal;
    font-family: "Arimo", sans-serif; font-size: 11px; line-height: 14px; color: var(--grey-text);
  }
  .indicia {
    position: absolute; left: 612px; top: 18px; width: 82px; height: 79px;
    border: 1px solid #555; text-align: center;
    font-family: "Arimo", sans-serif; font-size: 10.5px; line-height: 13px;
    padding-top: 7px; color: #222;
  }
  .indicia b { font-weight: 700; }
  .mail-panel {
    position: absolute; left: 480px; top: 134px; width: 214px; height: 86px;
    border: 1px solid #555;
    font-family: "Arimo", sans-serif; color: #222;
  }
  .mail-panel .endorsement { position: absolute; right: 16px; top: 10px; font-size: 9.5px; }
  .mail-panel .recipient { position: absolute; left: 15px; top: 40px; font-size: 12.5px; line-height: 14px; }
</style>
</head>
<body>

<!-- Front side -->
<section class="card card--front">
  <div class="stage-lights" role="img" aria-label="Colourful stage with spotlight beams and lit floor"></div>
  <svg class="front-band" width="711" height="40" viewBox="0 0 711 40">
    <polygon points="0,0 711,0 711,6 356,34 0,6" fill="var(--brand-blue)"/>
    <polygon points="0,6 356,34 711,6 711,10 356,40 0,10" fill="var(--brand-cyan)"/>
  </svg>
  <div class="brand-name">Quiz Arena<br>Duel Halls</div>
  <div class="headline">#1 New Experience in the Twin Cities</div>
  <p class="audience">Great for team building, work outings, birthday celebrations, or just for fun with friends and family</p>

  <div class="coupon coupon--left">
    <div class="coupon__inner">
      <div class="coupon__value">20% <span>OFF</span></div>
      <div class="coupon__code">Promo Code: DUEL20FALL</div>
      <p class="coupon__terms">Good for 20% off a booking of fewer than 10 people in Oct or Nov. One use per customer. Visit our website, click Get Tickets and enter the code above. Subject to change without notice.</p>
    </div>
  </div>

  <div class="finally">Finally<br>YOU"RE ALL IN<br>in the QUIZ ARENA!</div>

  <div class="coupon coupon--right">
    <div class="coupon__inner">
      <div class="coupon__value">50% <span>OFF</span></div>
      <div class="coupon__code">Promo Code: ARENA50FALL</div>
      <p class="coupon__terms">Good for $50 off a booking of 10 or more people in Oct or Nov. One use per customer. Enter the code above when booking online, or mention this coupon for private group events. Subject to change without notice.</p>
    </div>
  </div>

  <div class="contact-bar">
    <span class="item">
      <svg width="16" height="16" viewBox="0 0 16 16"><circle cx="8" cy="8" r="7" fill="none" stroke="var(--yellow)" stroke-width="1.4"/><path d="M8 3.5a2.8 2.8 0 0 0-2.8 2.8C5.2 8.5 8 12 8 12s2.8-3.5 2.8-5.7A2.8 2.8 0 0 0 8 3.5z" fill="var(--yellow)"/></svg>
      4127 Larkmoor Rd S, Cedar Hollow, MN
    </span>
    <span class="item">
      <svg width="16" height="16" viewBox="0 0 16 16"><circle cx="8" cy="8" r="7" fill="none" stroke="var(--yellow)" stroke-width="1.4"/><path d="M5.2 4.3l1.3-.3.8 1.8-.9.7c.4.9 1.1 1.6 2 2l.7-.9 1.8.8-.3 1.3c-3 .3-5.7-2.4-5.4-5.4z" fill="var(--yellow)"/></svg>
      555-318-2741
    </span>
    <span class="item">
      <svg width="16" height="16" viewBox="0 0 16 16" fill="none" stroke="var(--yellow)" stroke-width="1.2"><circle cx="8" cy="8" r="7"/><ellipse cx="8" cy="8" rx="3" ry="7"/><line x1="1" y1="8" x2="15" y2="8"/></svg>
      quizarenaduelhalls.example
    </span>
  </div>
</section>

<!-- Back side -->
<section class="card card--back">
  <svg class="back-panel" width="711" height="463" viewBox="0 0 711 463">
    <defs>
      <radialGradient id="darkPanel" cx="40%" cy="50%" r="70%">
        <stop offset="0" stop-color="#33353b"/>
        <stop offset="1" stop-color="#17181b"/>
      </radialGradient>
      <linearGradient id="bandGrad" x1="0" y1="0" x2="1" y2="0">
        <stop offset="0" stop-color="#22c4f2"/>
        <stop offset="1" stop-color="#0a7fd0"/>
      </linearGradient>
    </defs>
    <polygon points="0,0 352,0 400,463 0,463" fill="url(#darkPanel)"/>
    <polygon points="352,0 368,0 416,463 400,463" fill="var(--brand-blue)"/>
    <polygon points="0,202 385,202 400,294 0,294" fill="url(#bandGrad)"/>
  </svg>
  <div class="brand-name">Quiz Arena<br>Duel Halls</div>
  <div class="headline">#1 New Experience in the Twin Cities</div>
  <div class="private">Private team building events available upon request</div>
  <div class="online">ONLINE BOOKINGS AVAILABLE NOW!</div>
  <div class="web-button">www.quizarenaduelhalls.example</div>
  <div class="social">
    <span class="item handle">
      <svg width="20" height="20" viewBox="0 0 20 20"><circle cx="10" cy="10" r="9" fill="none" stroke="var(--yellow)" stroke-width="1.5"/></svg>
      @QuizArenaDuelHalls
    </span>
    <span class="item phone">
      <svg width="22" height="22" viewBox="0 0 16 16"><circle cx="8" cy="8" r="7" fill="none" stroke="var(--yellow)" stroke-width="1.3"/><path d="M5.2 4.3l1.3-.3.8 1.8-.9.7c.4.9 1.1 1.6 2 2l.7-.9 1.8.8-.3 1.3c-3 .3-5.7-2.4-5.4-5.4z" fill="var(--yellow)"/></svg>
      555-318-2741
    </span>
  </div>

  <address class="return-address">4127 Larkmoor Rd S,<br>Cedar Hollow, MN<br>p: 555-318-2741</address>

  <div class="indicia">PRSRT STD<br>ECRWSS<br>U.S. Postage<br><b>PAID</b><br>RMCD RETAIL</div>

  <div class="mail-panel">
    <span class="endorsement">*****************ECRWSS****</span>
    <span class="recipient">Local<br>Postal Customer</span>
  </div>
</section>

</body>
</html>
```